WP website design (Vorne)

We need a wordpress design for an established auction and real estate company based in Kentucky. The winning design will incorporate a professional color scheme with company logo in a clean layout with specified widgets. The design needs to consider that this will be developed on a responsive theme. Colors will complement the colors in the logo.

Industry/Entity Type

Real Estate

Font styles to use
Sans Serif

Requirements
Must have
• - Navigation:
1) Home 2) Auctions 3) Real Estate Listings 4) Our Services 5) Why Auctions 6) About Us 7) Past Auctions 8) Contact Us

Homeage will have slideshow, please use stock real estate image as the initial slide. Homepage will have this content: "Martin Vorne Auctioneer Real Estate Broker

Buying or selling you can count on Martin Vorne Auctioneer to deliver a quality auction experience. We handle all the details from initial handshake to final payment. We are with you every step of the way giving our sellers the service and results they deserve. You only have one chance for a successful auction. Contact us today to see how our experience and know-how can work for you. We are confident that you will appreciate our higher standard of service."

Footer will have smaller company logo, and attached association logos and this contact info:
Phone: (270) 555-0148
Contacts: Martin Vorne
Email: martinvorne@mailbrook.example
Address: 482 Pellworth Lane • Bowling Green, KY 42917

Widgets:
1) email sign up 2) Social media (twitter, Youtube - can also be in header 3) News & Events Blog widget 4) testimonials blog 5) Featured Video widget
Nice to have
• Nice to Have:
- demonstrate the drop-down menu styling, e.g. under Auctions
-Upcoming Auctions
-Online Auctions
-Past Auctions

```html
<!DOCTYPE html>
<html lang="en">
<head>
<meta charset="utf-8">
<title>Martin Vorne Auctioneer Real Estate Broker</title>
<link rel="stylesheet" href="https://fonts.googleapis.com/css2?family=Arimo:wght@400;700&family=Raleway:wght@400;500&family=Lilita+One&family=Source+Sans+3:wght@400;600&display=swap">
<style>
:root{
  --yellow:#f4c214;
  --yellow-deep:#f0b81a;
  --blue:#1f5fb0;
  --blue-dark:#184f97;
  --ink:#222;
  --muted:#444;
  --panel:#f1f1f1;
  --panel-line:#d6d6d6;
  --bar-dark:#3a3a3a;
  --footer:#333333;
  --gold-text:#b08a10;
}
*{box-sizing:border-box;margin:0;padding:0}
html,body{width:907px;height:1200px;overflow:hidden}
body{
  position:relative;
  font-family:Arimo,Arial,sans-serif;color:var(--ink);
  background:linear-gradient(180deg,#ffffff 0%,#ffffff 55%,#fbe7a0 78%,var(--yellow) 100%);
}
.page{
  position:absolute;left:74px;top:0;width:757px;height:1112px;background:#fff;
  box-shadow:0 0 10px rgba(0,0,0,.35);overflow:hidden;
}
.hero{
  position:absolute;left:0;top:0;width:757px;height:472px;
  background:linear-gradient(180deg,#8d9a92 0%,#c9ccd0 40%,#b7bbc0 65%,#6f6a60 100%);
}
.header-shape{position:absolute;left:0;top:0}
.brand{position:absolute;left:14px;top:36px;display:flex;align-items:center;gap:7px}
.brand-square{width:22px;height:22px;background:var(--blue)}
.brand-name{font-family:"Source Sans 3",sans-serif;font-weight:600;font-size:22px;color:var(--blue)}
.social{position:absolute;left:502px;top:52px;display:flex;align-items:center}
.social-label{font-family:"Source Sans 3",sans-serif;font-size:18px;color:#3a3a3a;margin-right:17px}
.social-dot{width:28px;height:28px;border-radius:50%;margin-right:6px}
.dot-a{background:#1b4a83}.dot-b{background:#2aa6e0}.dot-c{background:#ef7d1a}.dot-d{background:#bdbdbd}
.slide-caption{position:absolute;right:0;background:var(--yellow);color:#fff}
.caption-title{top:336px;width:289px;height:43px;font-family:"Lilita One",sans-serif;font-size:31px;line-height:43px;padding-left:12px}
.caption-title .accent{color:var(--blue)}
.caption-sub{top:385px;width:346px;height:39px;font-family:Raleway,sans-serif;font-size:24px;line-height:39px;padding-left:18px}
.slide-dots{position:absolute;left:351px;top:444px;display:flex;gap:5px}
.slide-dots span{width:10px;height:10px;border-radius:50%;background:#333;border:2px solid #ddd}
.slide-dots .on{background:var(--yellow-deep);width:12px;height:12px;margin-top:-1px}
.rule{position:absolute;left:0;top:472px;width:757px;height:8px;background:var(--yellow)}
.nav{position:absolute;left:0;top:480px;width:757px;height:32px;background:var(--blue)}
.nav a{position:absolute;top:0;line-height:32px;font-size:10.5px;color:#fff;text-decoration:none}
.nav .sep{position:absolute;top:6px;width:1px;height:22px;background:var(--blue-dark)}
.dropdown{position:absolute;left:78px;top:520px;width:105px;height:83px;background:#111;border-radius:2px;padding:4px 3px}
.dropdown::before{content:"";position:absolute;left:48px;top:-6px;border:6px solid transparent;border-top:0;border-bottom-color:#111}
.dropdown a{display:block;height:23px;line-height:20px;font-size:9px;color:#fff;text-decoration:none;padding-left:6px;border-bottom:1px solid #333;margin-bottom:2px}
.dropdown a.active{background:var(--blue)}
.dropdown a::before{content:"» ";font-weight:700}
.tab{position:absolute;top:550px;height:32px;border-radius:3px 3px 0 0;font-family:"Source Sans 3",sans-serif;font-weight:600;font-size:15px;line-height:32px;padding-left:8px}
.tab-news{left:18px;width:150px;background:var(--blue);color:#fff}
.tab-plain{background:linear-gradient(#eee,#d9d9d9);color:#333;border:1px solid #ccc;border-bottom:0}
.news-box{position:absolute;left:18px;top:581px;width:502px;height:227px;border:1px solid var(--panel-line);border-radius:3px;background:#fff;padding:13px 9px}
.news-photo{position:absolute;left:9px;top:13px;width:148px;height:99px;background:linear-gradient(160deg,#8a8076,#b9ada0 50%,#a79d90)}
.news-head{position:absolute;left:170px;top:12px;width:322px}
.news-head h3{font-weight:400;font-size:12px;margin-bottom:3px}
.news-date{font-size:8px;color:var(--gold-text);margin-bottom:4px}
.body-text{font-size:9px;line-height:13.6px;text-align:justify;color:var(--ink)}
.news-body{position:absolute;left:9px;top:123px;width:484px}
.read-more{position:absolute;right:9px;bottom:6px;background:var(--blue-dark);color:#fff;font-size:9.5px;padding:2px 6px;border-radius:3px;text-decoration:none}
.widget{position:absolute;background:var(--panel);border:1px solid var(--panel-line);border-radius:4px}
.widget-bar{position:relative;height:29px;margin:2px 2px 0;background:linear-gradient(#5a5a5a,var(--bar-dark));border-radius:3px 3px 0 0;color:#fff;font-family:Raleway,sans-serif;font-size:18px;line-height:29px;padding-left:12px}
.widget-bar::after{content:"";position:absolute;left:22px;bottom:-7px;border:7px solid transparent;border-bottom:0;border-top-color:var(--bar-dark)}
.testimonial{left:542px;top:549px;width:204px;height:259px}
.avatar{position:absolute;left:25px;top:46px;width:54px;height:54px;border-radius:50%;background:radial-gradient(#6d6d6d,#2c2c2c);border:3px solid #fff;box-shadow:0 0 0 1px #999}
.client-name{position:absolute;left:87px;top:82px;font-style:italic;font-size:10px;color:#555}
.quote{position:absolute;left:14px;top:116px;width:182px;font-size:9px;line-height:13.6px;color:var(--ink)}
.divider{position:absolute;top:840px;height:215px;border-left:1px dashed #c8c8c8}
.w-video{left:29px;top:838px;width:210px;height:214px}
.w-signup{left:290px;top:836px;width:209px;height:214px}
.w-asset{left:544px;top:834px;width:203px;height:214px}
.widget .intro{position:absolute;left:9px;top:41px;width:192px;font-size:9px;line-height:13.6px}
.player{position:absolute;left:5px;top:72px;width:199px;height:137px;border:2px solid #ddd;background:#222}
.player-frame{height:114px;background:linear-gradient(180deg,#8fa9c2 0%,#b9c4cb 45%,#8b5c45 65%,#6f8f4c 100%);position:relative}
.play{position:absolute;left:74px;top:38px;width:45px;height:34px;background:rgba(20,20,20,.8);border-radius:4px}
.play::after{content:"";position:absolute;left:17px;top:9px;border:8px solid transparent;border-right:0;border-left:13px solid #fff}
.controls{display:flex;align-items:center;height:19px;font-size:8px;color:#fff;padding:0 6px;gap:7px}
.controls .track{flex:1;height:3px;background:#777}
.field{position:absolute;left:19px;width:178px;height:24px;border:1px solid #c6c6c6;border-radius:4px;background:linear-gradient(#e4e4e4,#f2f2f2);font-style:italic;font-size:9.5px;color:#999;line-height:22px;padding-left:7px}
.subscribe{position:absolute;left:129px;top:164px;width:68px;height:24px;background:linear-gradient(#5e5e5e,#2c2c2c);border:2px solid #bbb;border-radius:5px;color:#fff;font-weight:700;font-size:10.5px;line-height:20px;text-align:center}
.asset-photo{position:absolute;left:14px;top:52px;width:182px;height:73px;border:2px solid #fff;background:linear-gradient(180deg,#9fb070 0%,#3e9b3a 45%,#5c5d55 100%)}
.asset-date{position:absolute;left:14px;top:143px;font-weight:700;font-size:9.5px;color:var(--gold-text)}
.asset-text{position:absolute;left:14px;top:159px;width:180px;font-size:9px;line-height:12.4px}
.more{position:absolute;right:6px;bottom:8px;font-style:italic;font-size:8px;color:#333}
.footer{position:absolute;left:0;top:1112px;width:907px;height:88px;background:var(--footer)}
.badge{position:absolute;top:20px;height:38px;background:#9a9a9a;border-radius:3px}
.badge.round{border-radius:50%/45%}
.footer-brand{position:absolute;left:340px;top:20px;display:flex;align-items:center;gap:5px;font-family:"Source Sans 3",sans-serif;font-weight:600;font-size:13px;color:#d0d0d0}
.footer-brand i{display:block;width:12px;height:12px;background:#d0d0d0}
.contact{position:absolute;right:83px;top:15px;text-align:right;font-size:10px;line-height:15.2px;color:#fff}
</style>
</head>
<body>
<div class="page">
  <div class="hero" role="img" aria-label="Stock photo of a two-storey suburban house with grey siding and a garage"></div>
  <svg class="header-shape" width="757" height="200" viewBox="0 0 757 200">
    <path d="M0 0H757V166Q380 74 0 144Z" fill="#f4c214"/>
    <path d="M0 136Q380 70 757 158V176Q380 100 0 160Z" fill="#1f5fb0"/>
    <path d="M0 160Q380 100 757 176V190Q380 112 0 168Z" fill="#f4c214"/>
    <rect width="757" height="4" fill="#1f5fb0"/>
  </svg>
  <div class="brand"><span class="brand-square"></span><span class="brand-name">Martin Vorne</span></div>
  <div class="social">
    <span class="social-label">Social Media</span>
    <span class="social-dot dot-a"></span><span class="social-dot dot-b"></span><span class="social-dot dot-c"></span><span class="social-dot dot-d"></span>
  </div>
  <div class="slide-caption caption-title">Lorem Ipsum <span class="accent">dolor</span></div>
  <div class="slide-caption caption-sub">text of the printing industry</div>
  <div class="slide-dots"><span></span><span></span><span class="on"></span><span></span></div>
  <div class="rule"></div>

  <nav class="nav">
    <a style="left:27px">Home</a><span class="sep" style="left:75px"></span>
    <a style="left:86px">Auctions</a><span class="sep" style="left:146px"></span>
    <a style="left:159px">Real Estate Listings</a><span class="sep" style="left:274px"></span>
    <a style="left:283px">Our Services</a><span class="sep" style="left:366px"></span>
    <a style="left:376px">Why Auctions</a><span class="sep" style="left:460px"></span>
    <a style="left:470px">About Us</a><span class="sep" style="left:535px"></span>
    <a style="left:546px">Past Auctions</a><span class="sep" style="left:633px"></span>
    <a style="left:644px">Contact Us</a>
  </nav>

  <div class="tab tab-news">News</div>
  <div class="tab tab-plain" style="left:174px;width:122px">Auction Results</div>
  <div class="tab tab-plain" style="left:302px;width:134px">Alliance Auctions</div>

  <div class="news-box">
    <div class="news-photo" role="img" aria-label="Photo of bare trees in a dry field"></div>
    <div class="news-head">
      <h3>Upcoming Auctions</h3>
      <p class="news-date">May 15, 2012</p>
      <p class="body-text"><b>Lorem Ipsum is simply dummy text</b> of the printing and typesetting industry. Lorem Ipsum has been the industry's standard dummy text ever since the 1500s, when an unknown printer took a galley of type and scrambled it to make a type specimen book. It has survived not only five centuries, but also the leap into electronic typesetting.</p>
    </div>
    <p class="body-text news-body">Lorem Ipsum is simply dummy text of the printing and typesetting industry. Lorem Ipsum has been the industry's standard dummy text ever since the 1500s, when an unknown printer took a galley of type and scrambled it to make a type specimen book. It has survived not only five centuries, but also the leap into electronic typesetting Lorem Ipsum is simply dummy text of the printing and typesetting industry. Lorem Ipsum has been the industry's standard dummy text ever since the 1500s, when an unknown printer took a galley of type and scrambled it to make a type specimen book.</p>
    <a class="read-more">read more</a>
  </div>

  <div class="dropdown">
    <a class="active">Online Auctions</a>
    <a>Upcoming Auctions</a>
    <a>Past Auctions</a>
  </div>

  <div class="widget testimonial">
    <div class="widget-bar">Client’s Testimonial</div>
    <div class="avatar" role="img" aria-label="Client portrait"></div>
    <span class="client-name">Carl Redding</span>
    <p class="quote">“ simply dummy text of the printing and typesetting industry. Lorem Ipsum has been the industry's standard dummy text ever since the 1500s. simply dummy text of the printing and typesetting industry. Lorem Ipsum has been the industry's standard dummy text ever since the 1500s.”</p>
  </div>

  <span class="divider" style="left:264px"></span>
  <span class="divider" style="left:523px"></span>

  <div class="widget w-video">
    <div class="widget-bar">Featured Vedio</div>
    <p class="intro" style="top:42px">simply dummy text of the printing and typesetting industry. Lorem Ipsum has been</p>
    <div class="player">
      <div class="player-frame" role="img" aria-label="Video still of a brick house"><span class="play"></span></div>
      <div class="controls"><span>▶</span><span>00:00</span><span class="track"></span><span>00:00</span><span>▮▮</span></div>
    </div>
  </div>

  <div class="widget w-signup">
    <div class="widget-bar">E-mail sign Up Form</div>
    <p class="intro" style="left:12px;top:47px">simply dummy text of the printing and typesetting industry. Lorem Ipsum has been</p>
    <div class="field" style="top:93px">Email Address</div>
    <div class="field" style="top:129px">Password</div>
    <div class="subscribe">Subscribe</div>
  </div>

  <div class="widget w-asset">
    <div class="widget-bar">Asset For Sale Fader</div>
    <div class="asset-photo" role="img" aria-label="Photo of a crowd at an outdoor equipment auction"></div>
    <p class="asset-date">Saturday March 16, 2013 at 10:00 AM</p>
    <p class="asset-text">simply dummy text of the simply dummy text of the printing and typesetting industry printing and industry.</p>
    <span class="more">More Details »</span>
  </div>
</div>

<footer class="footer">
  <span class="badge round" style="left:84px;width:68px"></span>
  <span class="badge" style="left:162px;width:34px"></span>
  <span class="badge" style="left:210px;width:68px;height:30px;top:24px"></span>
  <span class="badge" style="left:293px;width:53px;height:30px;top:24px"></span>
  <span class="badge" style="left:359px;width:30px"></span>
  <div class="footer-brand" style="left:412px;top:30px"><i></i>Martin Vorne</div>
  <div class="contact">
    Phone: (270) 555-0148<br>
    Contacts: Martin Vorne<br>
    Email: martinvorne@mailbrook.example<br>
    Address: 482 Pellworth Lane • Bowling Green, KY 42917
  </div>
</footer>
</body>
</html>
```